Harvest Gate Fellowship Network needs a fresh new web design

We are an up and coming multicultural church that aims to bring people into a life changing encounter with God. We need a fresh and inviting website in order to increase our internet presence and make us easier to connect with.
Here are some of the basic requirements for the site:
• Clearly displayed address, service times, and contact info
• A staff profile page
• An area for a calendar with upcoming events and their details
• Social media buttons
• Group pages for the different ministries (youth, children’s church, men, etc…)
• An area for donations and eCommerce
• A resources page for assorted media (podcasts, sermons, videos, etc.…)
• An area for prayer requests.

Industry/Entity Type

Church

```html
<!DOCTYPE html>
<html lang="en">
<head>
<meta charset="utf-8">
<title>Harvest Gate Fellowship Network</title>
<link href="https://fonts.googleapis.com/css2?family=Raleway:wght@500;600&family=Oswald:wght@400;500&family=Signika:wght@600;700&family=Arimo:wght@400;700&display=swap" rel="stylesheet">
<style>
:root{
  --purple:#31069a;
  --yellow:#f3d925;
  --gold:#e4a20f;
  --green:#2cc86a;
  --donate:#5fb544;
  --page:#efefef;
  --text:#444;
  --footer:#2b2e27;
  --footer-head:#8c8f88;
  --cal-cell:#8d9ff0;
  --cal-fade:#e9e9ee;
}
*{margin:0;padding:0;box-sizing:border-box}
html,body{width:1033px;height:1200px;overflow:hidden;background:var(--page)}
.stage{width:1200px;height:1394px;position:relative;transform:scale(.86083);transform-origin:0 0;background:var(--page);font-family:Arimo,Arial,sans-serif;color:var(--text)}
.abs{position:absolute}

/* header */
.topbar{left:0;top:0;width:1200px;height:50px;background:var(--purple)}
.brand{left:100px;top:0;width:312px;height:110px;background:#fff;border-radius:0 0 16px 16px;box-shadow:0 3px 8px rgba(0,0,0,.25);display:flex;align-items:center;gap:12px;padding:0 16px}
.brand-dot{width:46px;height:46px;border-radius:50%;background:var(--purple);flex:none}
.brand-name{font-family:Raleway,sans-serif;font-weight:600;font-size:21px;line-height:25px;color:var(--purple)}
.nav{left:536px;top:0;height:50px;display:flex;font-size:15px}
.nav a{color:#fff;text-decoration:none;display:flex;align-items:center;padding:0 18px;border-right:1px solid rgba(255,255,255,.15)}
.nav a.active{background:var(--yellow);color:#5a4b1a}
.nav a:last-child{border:0}

/* hero */
.hero{left:0;top:50px;width:1200px;height:480px;background:linear-gradient(180deg,#6f8aa0 0%,#b9b6a4 35%,#f2d89a 50%,#d0a24a 62%,#8a6a2a 80%,#5a4a22 100%)}
.hero-curve{left:0;top:470px;width:1200px;height:90px}
.headline{left:0;top:219px;width:1200px;text-align:center;font-family:Signika,sans-serif;font-weight:700;font-size:30px;letter-spacing:-.6px;text-shadow:0 2px 3px rgba(0,0,0,.35)}
.headline .y{color:#f2c81a}.headline .p{color:var(--purple)}
.donate{left:504px;top:350px;width:194px;height:50px;background:linear-gradient(#77cc58,var(--donate));border:2px solid #a6e08c;border-radius:4px;color:#fff;font-family:Oswald,sans-serif;font-size:28px;text-align:center;line-height:44px;box-shadow:0 2px 5px rgba(0,0,0,.35)}

/* intro */
.intro-photo{left:128px;top:569px;width:349px;height:212px;background:#fff;padding:5px;box-shadow:0 1px 4px rgba(0,0,0,.3)}
.intro-photo div{width:100%;height:100%;background:linear-gradient(135deg,#2a1a14,#b06a4a 45%,#e7b08c 60%,#7a2a1c)}
.intro-title{left:494px;top:566px;font-family:Raleway,sans-serif;font-weight:500;font-size:22px;color:var(--purple)}
.intro-text{left:495px;top:596px;width:582px;font-size:12px;line-height:20px;text-align:justify}
.intro-text p+p{margin-top:20px}
.more{left:1034px;top:758px;font-size:12px;font-weight:700;color:var(--purple)}
.rule{left:110px;top:804px;width:975px;border-top:1px dotted #bbb}

/* cards */
.card{top:832px;width:218px}
.card .pic{height:104px}
.card .label{height:38px;color:#fff;font-family:Signika,sans-serif;font-weight:700;font-size:18px;line-height:40px;padding-left:8px}
.card p{margin-top:10px;font-size:12px;line-height:18px;text-align:justify}
.btn{display:inline-block;margin-top:8px;height:27px;line-height:27px;padding:0 10px;border-radius:6px;color:#fff;font-weight:700;font-size:12px}

/* calendar */
.cal{left:864px;top:832px;width:224px;height:246px;background:#fff}
.cal-head{height:30px;background:var(--purple);color:#fff;font-weight:700;font-size:15px;text-align:center;line-height:30px;position:relative}
.cal-arrow{position:absolute;top:7px;width:16px;height:16px;border-radius:50%;background:#fff}
.cal-days{display:grid;grid-template-columns:repeat(7,1fr);height:31px;align-items:center;font-size:8px;color:#555;text-align:center;border-bottom:2px solid var(--purple)}
.cal-grid{display:grid;grid-template-columns:repeat(7,31px);grid-auto-rows:30px;gap:1px;padding-left:1px}
.cal-grid span{background:var(--cal-cell);display:flex;align-items:center;justify-content:center;font-size:11px;color:#111}
.cal-grid .fade{background:var(--cal-fade);color:#888}
.cal-grid .today{background:#000;color:#fff}
.events{left:870px;top:1070px;width:217px;height:33px;background:var(--purple);color:#fff;font-size:16px;text-align:center;line-height:33px;border-radius:2px}

/* footer */
.footer{left:0;top:1152px;width:1200px;height:242px;background:var(--footer)}
.fhead{font-family:Oswald,sans-serif;font-size:19px;color:var(--footer-head)}
.flist{list-style:none;font-size:14px;color:#fff}
.flist li{height:26px}
.social li{height:39px;display:flex;align-items:center;gap:10px}
.social i{width:22px;height:22px;border-radius:50%;background:#d9d9d9;display:block}
.contact{font-size:14px;line-height:18px;color:#fff}
.contact b{display:block;margin-top:17px}
.foot-brand{left:780px;top:1238px;display:flex;align-items:center;gap:12px}
.foot-brand .brand-dot{background:#8f8f8f;width:60px;height:60px}
.foot-brand .brand-name{color:#9a9a9a;font-size:24px;line-height:28px}
</style>
</head>
<body>
<div class="stage">
  <div class="abs hero" role="img" aria-label="Person with raised arms in a golden wheat field at sunset"></div>
  <svg class="abs hero-curve" viewBox="0 0 1200 90" preserveAspectRatio="none"><path d="M0 15 Q600 85 1200 25 L1200 90 L0 90Z" fill="#efefef"/></svg>
  <div class="abs headline"><span class="y">LETS MAKE A DIFFERENCE...</span> <span class="p">FOR THE CHILDREN'S FUTURE</span></div>
  <div class="abs donate">DONATE NOW</div>

  <div class="abs topbar"></div>
  <div class="abs brand"><span class="brand-dot"></span><span class="brand-name">Harvest Gate<br>Fellowship Network</span></div>
  <nav class="abs nav">
    <a class="active">Who we are</a><a style="padding:0 26px 0 42px">What we do</a><a>Get Involved</a><a>News</a><a>Contact Us</a>
  </nav>

  <div class="abs intro-photo"><div role="img" aria-label="Hands clasped in prayer"></div></div>
  <h1 class="abs intro-title">Harvest Gate Fellowship Network</h1>
  <div class="abs intro-text">
    <p>Lorem Ipsum is simply dummy text of the printing and typesetting industry. Lorem Ipsum has been the industry's standard dummy text ever since the 1500s, when an unknown printer took a galley of type and scrambled it to make a type specimen book. It has survived not only five centuries, but also the leap into electronic typesetting, remaining essentially unchanged. It was popularised in the 1960s with the release of Printwell with the release of Printwell sheets containing Lorem Ipsum passages, and more recently with desktop.</p>
    <p>Printwell sheets containing Lorem Ipsum passages, and more recently with desktop publishing software like PageForge Studio including versions of Lorem Ipsum.</p>
  </div>
  <div class="abs more">MORE.</div>
  <div class="abs rule"></div>

  <div class="abs card" style="left:118px">
    <div class="pic" role="img" aria-label="Woman with head bowed in prayer" style="background:linear-gradient(135deg,#f2efe9,#6b4a3a 55%,#c9c4bd)"></div>
    <div class="label" style="background:var(--gold)">OUR STAFF</div>
    <p>Lorem Ipsum is simply dummy text of the printing and typesetting industry. Lorem Ipsum has been the industry's standard dummy text ever since the 1500s, when an un.</p>
    <span class="btn" style="background:var(--gold)">READMORE</span>
  </div>
  <div class="abs card" style="left:355px">
    <div class="pic" role="img" aria-label="Congregation praying during a service" style="background:linear-gradient(135deg,#3a2a26,#8a6a5a 50%,#1e1a1c)"></div>
    <div class="label" style="background:var(--purple)">MINISTRIES</div>
    <p>Lorem Ipsum is simply dummy text of the printing and typesetting industry. Lorem Ipsum has been the industry's standard dummy text ever since the 1500s, when an un.</p>
    <span class="btn" style="background:var(--purple);margin-left:4px">READMORE</span>
  </div>
  <div class="abs card" style="left:601px">
    <div class="pic" role="img" aria-label="Child praying in soft light" style="background:linear-gradient(135deg,#dfe6d4,#b8c9a4 40%,#c87a4a 70%,#e9c9a4)"></div>
    <div class="label" style="background:var(--green)">PRAYER REQUESTS</div>
    <p style="padding-left:5px">Lorem Ipsum is simply dummy text of the printing and typesetting industry. Lorem Ipsum has been the industry's standard dummy text ever since the 1500s, when an un</p>
    <span class="btn" style="background:var(--green);margin-left:7px">READMORE</span>
  </div>

  <div class="abs cal">
    <div class="cal-head"><span class="cal-arrow" style="left:10px"></span>March 2013<span class="cal-arrow" style="right:10px"></span></div>
    <div class="cal-days"><span>MON</span><span>TUE</span><span>WED</span><span>THU</span><span>FRI</span><span>SAT</span><span>SUN</span></div>
    <div class="cal-grid">
      <span class="fade">28</span><span>1</span><span>2</span><span>3</span><span class="today">4</span><span>5</span><span>6</span>
      <span>7</span><span>8</span><span>9</span><span>10</span><span>11</span><span>12</span><span>13</span>
      <span>14</span><span>15</span><span>16</span><span>17</span><span></span><span>19</span><span>20</span>
      <span>21</span><span>22</span><span>23</span><span>24</span><span>25</span><span>26</span><span>27</span>
      <span>28</span><span>29</span><span>30</span><span>31</span><span class="fade">1</span><span class="fade">2</span><span class="fade">3</span>
    </div>
  </div>
  <div class="abs events">UPCOMING EVENTS</div>

  <footer class="abs footer"></footer>
  <div class="abs fhead" style="left:137px;top:1168px">ABOUT US</div>
  <ul class="abs flist" style="left:139px;top:1207px">
    <li>Home</li><li>Who We Are</li><li>What We Do</li><li>Get Involved</li><li>Support Us</li><li style="margin-top:3px">News</li><li style="margin-top:1px">Contact Us</li>
  </ul>
  <div class="abs fhead" style="left:358px;top:1168px">FOLLOW US</div>
  <ul class="abs flist social" style="left:358px;top:1203px">
    <li><i></i>Gatherbook</li><li><i></i>Chirpline</li><li><i></i>StreamHall</li><li><i></i>RSS</li>
  </ul>
  <div class="abs fhead" style="left:568px;top:1168px">CONTACT US</div>
  <div class="abs contact" style="left:570px;top:1214px">
    PO BOX 418<br>Millbrook Falls<br>Ohio, 43920
    <b>CALL US</b>555-210-4437
    <b>EMAIL US</b>hello@harvestgate.org
  </div>
  <div class="abs foot-brand"><span class="brand-dot"></span><span class="brand-name">Harvest Gate<br>Fellowship Network</span></div>
</div>
</body>
</html>
```